Lawn Sign Design – Brisko

We need a clean, eye-catching 18" x 24" lawn sign for Brisko that effectively communicates our core message while maintaining strong brand consistency.

Key Elements to Include:
Tagline (Main Focus): Upgrade Your Roof Without Replacing It
Website: www.tryvexlo-demo.example
Phone Number: (877) BRISKO-GO
RQMH License Number: 4830516
Brisko Logo & Branding: Ensure the logo, corporate colors, and custom font are used consistently to align with our existing branding.

Design Guidelines:
Simple & High-Impact: The tagline should be the most prominent element on the sign, drawing immediate attention.
Easy Readability: Use a bold, clean design with high contrast for quick readability from a distance.
Balanced Layout: Place supporting details (website, phone number, and RQMH number) in a visually clear but secondary position to the tagline.
Professional & Modern: The sign should reflect credibility and innovation in the roofing industry.

Deliverables:
High-resolution print-ready files (CMYK)
A digital proof for review before finalizing
The final design should make a strong impression with minimal text, ensuring that anyone passing by can instantly grasp what we offer.

I am including our custom font. To get an hexagon in our name, simply type the $ after the 'O" Please use this font for anything you type.

```html
<!DOCTYPE html>
<html lang="en">
<head>
<meta charset="utf-8">
<title>Brisko Lawn Sign</title>
<link rel="stylesheet" href="https://fonts.googleapis.com/css2?family=Poppins:wght@500;600;700;800&display=swap">
<style>
  :root {
    --backdrop: #979797;
    --brand-blue: #185196;
    --ink-dark: #404040;
    --ink-black: #05090d;
    --paper: #ffffff;
  }
  html, body {
    margin: 0;
    padding: 0;
    overflow: hidden;
  }
  .canvas {
    position: relative;
    width: 914px;
    height: 1200px;
    background: var(--backdrop);
    overflow: hidden;
    font-family: "Poppins", sans-serif;
  }
  .sign-art {
    position: absolute;
    left: 0;
    top: 0;
    width: 914px;
    height: 1200px;
  }
  .line {
    position: absolute;
    left: 0;
    width: 914px;
    margin: 0;
    text-align: center;
    line-height: 1;
    white-space: nowrap;
    text-transform: uppercase;
  }
  .brand {
    position: absolute;
    left: 214px;
    top: 176px;
    display: flex;
    align-items: center;
    gap: 24px;
  }
  .brand-dot {
    width: 74px;
    height: 74px;
    border: 9px solid var(--paper);
    border-radius: 50%;
    box-sizing: border-box;
  }
  .brand-name {
    font-size: 84px;
    font-weight: 600;
    color: var(--paper);
    line-height: 1;
    letter-spacing: 1px;
  }
  .tagline-upgrade {
    top: 471px;
    font-size: 60px;
    font-weight: 800;
    color: var(--ink-dark);
    letter-spacing: -0.5px;
  }
  .tagline-roof {
    top: 527px;
    font-size: 116px;
    font-weight: 800;
    color: var(--brand-blue);
    letter-spacing: -1px;
  }
  .tagline-without {
    top: 645px;
    font-size: 66px;
    font-weight: 500;
    color: var(--brand-blue);
  }
  .tagline-replacing {
    top: 708px;
    font-size: 64px;
    font-weight: 800;
    color: var(--ink-dark);
    letter-spacing: -1px;
  }
  .license {
    top: 810px;
    font-size: 37px;
    font-weight: 700;
    color: var(--ink-dark);
    text-transform: none;
    letter-spacing: -0.5px;
  }
  .license-number {
    color: var(--brand-blue);
    font-weight: 600;
  }
  .phone-pill {
    position: absolute;
    left: 161px;
    top: 875px;
    width: 593px;
    height: 89px;
    background: var(--ink-black);
    border-radius: 20px;
    display: flex;
    align-items: center;
    box-sizing: border-box;
    padding-left: 21px;
    gap: 12px;
  }
  .phone-icon {
    width: 64px;
    height: 64px;
    flex: none;
  }
  .phone-number {
    font-size: 49px;
    font-weight: 600;
    color: var(--paper);
    line-height: 1;
    white-space: nowrap;
    letter-spacing: 0.5px;
  }
  .website {
    top: 993px;
    font-size: 43px;
    font-weight: 700;
    color: var(--ink-black);
    text-transform: none;
    letter-spacing: -0.5px;
  }
</style>
</head>
<body>
<main class="canvas">
  <svg class="sign-art" viewBox="0 0 1500 1970" aria-hidden="true">
    <rect class="sign-shadow" x="160" y="199" width="1186" height="1580" fill="#000" opacity="0.12"/>
    <rect class="sign-field" x="157" y="195" width="1186" height="1383" fill="var(--brand-blue)"/>
    <rect class="sign-footer" x="157" y="1578" width="1186" height="197" fill="var(--paper)"/>
    <polygon class="sign-panel" points="168,793 750,447 1333,793 1333,1490 1240,1545 265,1545 168,1490" fill="var(--paper)"/>
    <polyline class="header-frame" points="302,195 302,473 508,595" fill="none" stroke="var(--paper)" stroke-width="5"/>
    <polyline class="header-frame" points="1198,195 1198,473 995,593" fill="none" stroke="var(--paper)" stroke-width="5"/>
    <polyline class="header-point" points="508,597 750,740 995,597" fill="none" stroke="var(--brand-blue)" stroke-width="5"/>
  </svg>

  <div class="brand">
    <span class="brand-dot"></span>
    <span class="brand-name">BRISKO</span>
  </div>

  <h1 class="line tagline-upgrade">Upgrade Your</h1>
  <p class="line tagline-roof">Roof</p>
  <p class="line tagline-without">Without</p>
  <p class="line tagline-replacing">Replacing It</p>

  <p class="line license">RQMH License Number: <span class="license-number">4830516</span></p>

  <div class="phone-pill">
    <svg class="phone-icon" viewBox="0 0 64 64" aria-hidden="true">
      <circle cx="32" cy="32" r="32" fill="var(--paper)"/>
      <path d="M20 15c2-1 4 0 5 2l3 6c1 2 0 4-1 5l-2 2c2 5 6 9 11 11l2-2c1-1 3-2 5-1l6 3c2 1 3 3 2 5l-2 4c-1 2-4 3-7 2-11-3-20-12-23-23-1-3 0-6 2-7z" fill="var(--ink-black)"/>
      <path d="M36 17a12 12 0 0 1 11 11M36 23a6 6 0 0 1 5 5" fill="none" stroke="var(--ink-black)" stroke-width="3" stroke-linecap="round"/>
    </svg>
    <span class="phone-number">(877) BRISKO-GO</span>
  </div>

  <p class="line website">www.tryvexlo-demo.example</p>
</main>
</body>
</html>
```